Fernbrook Plots - Online-only garden installation company

Online-only garden installation company. Our demographic is middle aged / suburban women, and we anticipate Facebook driving traffic to this website, as well as referrals from garden centers. The website must be very simple in design and function.

All orders will be placed through the website, including size of garden (3 options), location in yard, payment, and scheduling of installation date.

The website should employ a 3 step process:

Step 1: Select garden size. Either an 4' X 4', 8' X 4', or 12' X 4'.

Step 2: Select a location. We would like to use google maps to look up a US address, then "drag and drop" one of the garden sizes from step 1 to the location the customer would like us to install the garden at their home.

Step 3: Pick an installation date and pay. Using an online calendar the customer will pick a date, and then pay for the installation via credit card.

The website will be linked to an email account, FernbrookPlots@mailvessel.com to inform us of orders placed.

Target Market(s)

Our demographic is middle aged / suburban women, and we anticipate Facebook driving traffic to this website, as well as referrals from garden centers.

Industry/Entity Type

It Company

Coding

Coded - Design and coding required

Number of Pages Required

4 page

Requirements
Must have
• Scheduling and payment options.

```html
<!DOCTYPE html>
<html lang="en">
<head>
<meta charset="utf-8">
<title>Fernbrook Plots – Garden Installation Company</title>
<link href="https://fonts.googleapis.com/css2?family=Roboto+Slab:wght@300;400;700&family=Open+Sans:wght@400;600;700&display=swap" rel="stylesheet">
<style>
:root{
  --green:#3a7d36;
  --green-dark:#2f6a2c;
  --orange:#e05a26;
  --orange-deep:#d24f1c;
  --ink:#333;
  --muted:#666;
  --light:#f3f4f5;
  --line:#dcdcdc;
  --white:#fff;
}
*{box-sizing:border-box;margin:0;padding:0}
html,body{width:1200px;height:2862px;overflow:hidden;background:var(--white)}
body{position:relative;font-family:"Open Sans",Arial,sans-serif;color:var(--ink)}
.abs{position:absolute}

/* header */
.header{left:0;top:0;width:1200px;height:103px;background:var(--white)}
.topbar{left:700px;top:0;width:500px;height:42px;background:var(--green);display:flex;align-items:center;padding-left:30px;gap:10px;color:var(--white);font-size:16px;font-weight:600;clip-path:polygon(22px 0,100% 0,100% 100%,0 100%)}
.topbar .socials{display:flex;gap:6px;margin-left:10px}
.topbar .socials span{width:26px;height:26px;border:2px solid var(--white);border-radius:50%}
.nav{right:22px;top:68px;display:flex;align-items:center;font-size:12.5px;color:#555;font-weight:600}
.nav a{color:#555;text-decoration:none;padding:0 26px;letter-spacing:.3px}
.nav a:last-of-type{padding-right:12px;border-right:1px solid #ccc}
.nav .search{margin-left:12px}
.logo-badge{left:86px;top:-4px;width:166px;height:176px;border-radius:50%;background:var(--white);z-index:3;display:flex;align-items:center;justify-content:center;text-align:center}
.logo-badge span{font-family:"Roboto Slab",Georgia,serif;font-weight:700;font-size:23px;line-height:1.1;color:var(--green)}

/* hero */
.hero{left:0;top:103px;width:1200px;height:536px;background:radial-gradient(ellipse at 75% 60%,#d86a2c 0,#b6592a 14%,#5e4a2e 34%,#3e3a26 60%,#4e6a2e 100%)}
.hero-title{left:86px;top:338px;color:var(--white);font-family:"Roboto Slab",Georgia,serif}
.hero-title h1{font-size:40px;font-weight:700}
.hero-title p{font-size:40px;font-weight:300;margin-top:8px}
.dots{left:98px;top:610px;display:flex;gap:6px}
.dots span{width:15px;height:15px;border:2px solid var(--white);border-radius:50%}
.dots span.on{background:var(--orange)}

/* section headings */
.sec-title{left:0;width:1200px;text-align:center;font-family:"Roboto Slab",Georgia,serif;font-size:30px;color:var(--orange)}
.sec-sub{left:0;width:1200px;text-align:center;font-size:11.5px;color:var(--muted)}

/* process */
.step{width:360px;text-align:center}
.step .ring{width:124px;height:124px;border-radius:50%;border:4px solid var(--green);padding:5px;margin:0 auto}
.step .ring div{width:100%;height:100%;border-radius:50%;display:flex;align-items:center;justify-content:center}
.step h3{font-family:"Roboto Slab",Georgia,serif;font-weight:400;font-size:18px;color:var(--green);margin-top:32px}
.step h3.orange{color:var(--orange)}
.step p{font-size:11.5px;line-height:25px;color:var(--muted);margin-top:10px}

/* address */
.address{left:0;top:1078px;width:1200px;height:439px;background:radial-gradient(#dfe1e3 1.3px,transparent 1.6px) 0 0/8px 8px,var(--light)}
.search-box{left:363px;top:1272px;width:473px;height:37px;background:var(--white);border:1px solid #e2e2e2;font-size:11px;color:#999;padding:0 14px;display:flex;align-items:center;justify-content:space-between}

/* form */
.form-photo{left:0;top:1517px;width:597px;height:435px;background:linear-gradient(180deg,#7ea84a 0,#5d8a36 40%,#6b4a2c 72%,#3d2b1c 100%)}
.form-panel{left:597px;top:1517px;width:603px;height:435px;background:var(--orange)}
.form-panel h2{position:absolute;left:0;top:62px;width:100%;text-align:center;font-family:"Roboto Slab",Georgia,serif;font-weight:400;font-size:30px;color:var(--white)}
.form-panel .sub{position:absolute;left:0;top:110px;width:100%;text-align:center;font-size:11.5px;color:var(--white)}
.field{left:99px;width:390px;height:38px;background:var(--white);border-radius:3px;font-size:13px;color:#555;padding:0 14px;display:flex;align-items:center;justify-content:space-between}
.submit{left:237px;top:345px;width:112px;height:36px;background:var(--green);color:var(--white);font-size:14px;font-weight:700;display:flex;align-items:center;justify-content:center;letter-spacing:.5px}

/* blog */
.post{top:2085px;width:325px}
.post .img{height:206px}
.post h4{font-family:"Roboto Slab",Georgia,serif;font-weight:400;font-size:16px;margin-top:25px;padding-bottom:14px;border-bottom:1px solid var(--line)}
.post .meta{display:flex;justify-content:space-between;font-size:8.5px;color:#777;padding:12px 0;border-bottom:1px solid var(--line)}
.post p{font-size:11.3px;line-height:25px;color:#444;margin-top:10px}

/* footer */
.footer{left:0;top:2532px;width:1200px;height:263px;background:var(--light)}
.foot-logo{left:118px;top:2600px;width:210px;text-align:center;font-family:"Roboto Slab",Georgia,serif;font-weight:700;font-size:28px;line-height:1.15;color:var(--green)}
.foot-h{top:2579px;font-size:15px;font-weight:600;color:#333;letter-spacing:.5px}
.contact-list{left:382px;top:2630px;font-size:12px;color:#555;list-style:none}
.contact-list li{display:flex;gap:12px;margin-bottom:10px;line-height:15px}
.contact-list li span.ic{width:14px;flex:none;color:#777}
.contact-list a{color:#555}
.news-text{left:628px;top:2625px;width:220px;font-size:12px;line-height:20px;color:#777}
.email-input{left:628px;top:2673px;width:212px;height:34px;background:var(--white);border:1px solid #ccc;font-size:11px;padding:0 12px;display:flex;align-items:center;color:#444}
.subscribe{left:628px;top:2715px;width:82px;height:30px;background:var(--orange);color:var(--white);font-size:10px;font-weight:700;display:flex;align-items:center;justify-content:center}
.follow-text{left:885px;top:2625px;width:230px;font-size:12px;line-height:20px;color:#888}
.follow-icons{left:885px;top:2698px;display:flex;gap:8px}
.follow-icons span{width:34px;height:34px;border:1px solid #aaa;border-radius:50%}
.bottom{left:0;top:2795px;width:1200px;height:67px;background:var(--green);color:var(--white);font-size:11.5px;display:flex;align-items:center;justify-content:center}
</style>
</head>
<body>

<header class="abs header">
  <div class="abs topbar">
    <svg width="16" height="16" viewBox="0 0 24 24" fill="#fff"><path d="M6.6 10.8a15 15 0 006.6 6.6l2.2-2.2c.3-.3.7-.4 1-.2 1.1.4 2.3.6 3.6.6.6 0 1 .4 1 1V20c0 .6-.4 1-1 1A17 17 0 013 4c0-.6.4-1 1-1h3.5c.6 0 1 .4 1 1 0 1.3.2 2.5.6 3.6.1.3 0 .7-.2 1z"/></svg>
    <span>CALL US : (000)-555-0148</span>
    <div class="socials"><span></span><span></span><span></span><span></span><span></span></div>
  </div>
  <div class="abs logo-badge"><span>Fernbrook<br>Plots</span></div>
  <nav class="abs nav">
    <a href="#">HOME</a><a href="#">ABOUT US</a><a href="#">SERVICES</a><a href="#">PRODUCTS</a><a href="#">HOW IT WORKS</a><a href="#">CONTACT US</a>
    <svg class="search" width="12" height="12" viewBox="0 0 24 24" fill="none" stroke="#e05a26" stroke-width="3"><circle cx="10" cy="10" r="7"/><path d="M15 15l7 7"/></svg>
  </nav>
</header>

<section class="abs hero" role="img" aria-label="Close-up photo of a carrot growing in garden soil"></section>
<div class="abs hero-title"><h1>Fernbrook Plots</h1><p>Garden Installation Company</p></div>
<div class="abs dots"><span></span><span class="on"></span><span></span><span></span></div>

<h2 class="abs sec-title" style="top:670px;font-weight:400">Our Process</h2>
<p class="abs sec-sub" style="top:719px">Sed ut perspiciatis unde omnis iste natus error sit voluptatem accusantium doloremque laudantium</p>

<div class="abs step" style="left:64px;top:779px">
  <div class="ring"><div style="background:var(--orange)">
    <svg width="56" height="56" viewBox="0 0 56 56" fill="none" stroke="#fff" stroke-width="2.5"><path d="M6 48l10-18h24l10 18z"/><circle cx="28" cy="16" r="8"/><path d="M28 24v12M16 40h4M30 40h4M24 44h4"/></svg>
  </div></div>
  <h3>Select Garden Size</h3>
  <p>Sed ut perspiciatis unde omnis iste natus error sit<br>voluptatem accusantium doloremque laudantium,<br>eaque ipsa dicta sunt explicabo.</p>
</div>
<div class="abs step" style="left:421px;top:779px">
  <div class="ring"><div style="background:var(--green)">
    <svg width="50" height="56" viewBox="0 0 50 56" fill="none" stroke="#fff" stroke-width="2.5"><path d="M25 44S12 30 12 20a13 13 0 0126 0c0 10-13 24-13 24z"/><circle cx="25" cy="20" r="5"/><ellipse cx="25" cy="48" rx="14" ry="4"/></svg>
  </div></div>
  <h3 class="orange">Select a Location</h3>
  <p>Sed ut perspiciatis unde omnis iste natus error sit<br>voluptatem accusantium doloremque laudantium,<br>eaque ipsa dicta sunt explicabo.</p>
</div>
<div class="abs step" style="left:776px;top:779px">
  <div class="ring"><div style="background:var(--orange)">
    <svg width="56" height="56" viewBox="0 0 56 56" fill="none" stroke="#fff" stroke-width="2.5"><rect x="6" y="10" width="38" height="34" rx="2"/><path d="M6 20h38M15 6v8M35 6v8M12 26h6M22 26h6M12 33h6M22 33h6"/><circle cx="40" cy="40" r="10" fill="#e05a26"/><path d="M40 34v12M43 36h-5a2 2 0 000 4h4a2 2 0 010 4h-5"/></svg>
  </div></div>
  <h3>Installation Date &amp; Pay</h3>
  <p>Sed ut perspiciatis unde omnis iste natus error sit<br>voluptatem accusantium doloremque laudantium,<br>eaque ipsa dicta sunt explicabo.</p>
</div>

<section class="abs address" role="img" aria-label="Dotted world map with location pins"></section>
<svg class="abs" style="left:0;top:1078px" width="1200" height="439" viewBox="0 0 1200 439">
  <defs><path id="pin" d="M0 0a11 11 0 0111 11c0 8-11 19-11 19S-11 19-11 11A11 11 0 010 0z"/></defs>
  <g fill="#fff" stroke-width="4">
    <use href="#pin" x="138" y="34" stroke="#e5b21c"/><use href="#pin" x="233" y="45" stroke="#7cb342"/>
    <use href="#pin" x="311" y="119" stroke="#b0226f"/><use href="#pin" x="207" y="146" stroke="#2d6cb0"/>
    <use href="#pin" x="295" y="241" stroke="#b0226f"/><use href="#pin" x="384" y="259" stroke="#1aa1a9"/>
    <use href="#pin" x="298" y="325" stroke="#1aa1a9"/><use href="#pin" x="798" y="42" stroke="#e5b21c"/>
    <use href="#pin" x="890" y="55" stroke="#7cb342"/><use href="#pin" x="968" y="122" stroke="#b0226f"/>
    <use href="#pin" x="866" y="149" stroke="#2d6cb0"/><use href="#pin" x="954" y="249" stroke="#b0226f"/>
    <use href="#pin" x="1043" y="267" stroke="#1aa1a9"/><use href="#pin" x="957" y="330" stroke="#1aa1a9"/>
  </g>
</svg>
<h2 class="abs sec-title" style="top:1188px;font-weight:400">Select Address</h2>
<p class="abs sec-sub" style="top:1236px">Sed ut perspiciatis unde omnis iste natus error sit voluptatem accusantium doloremque</p>
<div class="abs search-box">Search Your Address :<svg width="10" height="6" viewBox="0 0 10 6"><path d="M0 0h10L5 6z" fill="#888"/></svg></div>

<section class="abs form-photo" role="img" aria-label="Photo of carrots growing in rich soil"></section>
<section class="abs form-panel">
  <h2>Installation Form</h2>
  <p class="sub">Sed ut perspiciatis unde omnis iste natus error sit voluptatem accusantium</p>
  <div class="abs field" style="top:152px">Size of Garden :<svg width="10" height="6" viewBox="0 0 10 6"><path d="M0 0h10L5 6z" fill="#888"/></svg></div>
  <div class="abs field" style="top:196px">Location in Yard :<svg width="10" height="14" viewBox="0 0 10 14" fill="none" stroke="#888" stroke-width="1.6"><path d="M5 13S1 8 1 5a4 4 0 018 0c0 3-4 8-4 8z"/><circle cx="5" cy="5" r="1.4"/></svg></div>
  <div class="abs field" style="top:242px">Payment :<svg width="14" height="10" viewBox="0 0 14 10" fill="none" stroke="#888" stroke-width="1.4"><rect x=".7" y=".7" width="12.6" height="8.6" rx="1"/><path d="M.7 3.5h12.6"/></svg></div>
  <div class="abs field" style="top:286px">Installation Date :<svg width="12" height="12" viewBox="0 0 12 12" fill="none" stroke="#888" stroke-width="1.4"><rect x=".7" y="1.7" width="10.6" height="9.6"/><path d="M.7 4.5h10.6M3.5 0v3M8.5 0v3"/></svg></div>
  <div class="abs submit">SUBMIT</div>
</section>

<h2 class="abs sec-title" style="top:1991px;font-weight:400">Latest Blog</h2>
<p class="abs sec-sub" style="top:2039px">Sed ut perspiciatis unde omnis iste natus error sit voluptatem accusantium doloremque laudantium</p>

<article class="abs post" style="left:86px">
  <div class="img" role="img" aria-label="Photo of a hand pulling fresh carrots from a leafy garden bed" style="background:linear-gradient(160deg,#6f9a3e,#3f6b25 55%,#8a4a2a)"></div>
  <h4>Sed ut perspiciatis unde omnis</h4>
  <div class="meta"><span>27 MARCH 2016</span><span>120</span><span>LIKE</span><span>SHARE</span></div>
  <p>Sed ut perspiciatis unde omnis iste natus error sit volupta-tem accusantium doloremque laudantium, totam rem ape architecto beatae vitae dicta sunt explicabo.</p>
</article>
<article class="abs post" style="left:439px">
  <div class="img" role="img" aria-label="Photo of harvested carrots lying on dark soil" style="background:linear-gradient(135deg,#4a3222,#d9662a 45%,#5a3a24 80%)"></div>
  <h4>Sed ut perspiciatis unde omnis</h4>
  <div class="meta"><span>27 MARCH 2016</span><span>120</span><span>LIKE</span><span>SHARE</span></div>
  <p>Sed ut perspiciatis unde omnis iste natus error sit volupta-tem accusantium doloremque laudantium, totam rem ape architecto beatae vitae dicta sunt explicabo.</p>
</article>
<article class="abs post" style="left:790px">
  <div class="img" role="img" aria-label="Photo of harvested carrots lying on dark soil" style="background:linear-gradient(135deg,#4a3222,#d9662a 45%,#5a3a24 80%)"></div>
  <h4>Sed ut perspiciatis unde omnis</h4>
  <div class="meta"><span>27 MARCH 2016</span><span>120</span><span>LIKE</span><span>SHARE</span></div>
  <p>Sed ut perspiciatis unde omnis iste natus error sit volupta-tem accusantium doloremque laudantium, totam rem ape architecto beatae vitae dicta sunt explicabo.</p>
</article>

<footer class="abs footer"></footer>
<div class="abs foot-logo">Fernbrook<br>Plots</div>

<h5 class="abs foot-h" style="left:382px">CONTACT US</h5>
<ul class="abs contact-list">
  <li><span class="ic">☎</span>(000)-555-0148 (Phone)</li>
  <li><span class="ic">⎙</span>(000)-555-0148 (Fax)</li>
  <li><span class="ic">✉</span><a href="#">info@FernbrookPlots.com</a></li>
  <li><span class="ic"><svg width="10" height="14" viewBox="0 0 10 14" fill="#777"><path d="M5 14S0 8 0 5a5 5 0 0110 0c0 3-5 9-5 9z"/></svg></span>70 Lorem Ipsum Dummy Text<br>Lorem Ipsum</li>
</ul>

<h5 class="abs foot-h" style="left:628px">NEWSLETTER</h5>
<p class="abs news-text">Register Your email address to get information ablout us</p>
<div class="abs email-input">Email Address</div>
<div class="abs subscribe">SUBSCRIBE</div>

<h5 class="abs foot-h" style="left:885px">FOLLOW US</h5>
<p class="abs follow-text">Lorem ipsum dolor sit amet, conse ctetur adipiscing elit. Nulla in purus nibh. Donec ornare</p>
<div class="abs follow-icons"><span></span><span></span><span></span><span></span><span></span></div>

<div class="abs bottom">© Copyright 2017 Fernbrook Plots.All Rights Reserved</div>

</body>
</html>
```